Website Redesign for Mortgage, Property and Conveyancing business

Project Overview:
We are looking for a refresh and redesign of our current website to a smart, crisp and fresh approach to Home Loans, Conveyancing and Property sales. This task will be to:
- Redesign our current website in accordance with the new wireframe.
- Provide all elements required for the design
- Build 7 key templates including:
Home Page
2nd Level Section Page
3rd level Product landing Page
2nd Level - About Us, Contact Us etc
Blog
Blog Article
Campaign Page - no header
Technical
The design is for a Wordpress website. Existing theme is Quartzline and we use Elementor for page editing. We are open to a new theme to be introduced but would prefer to stay with elementor.
Current Site is: www.bluecanopy.com.au
Sites that we like or elements of sites:
Marlow Real Estate: https://www.marlow.com.au/ (Like use of video and navigation)
Copper Lantern Way - Mortage: https://clw.com.au/refinance-home-loan/ (Like landing pages a sin example)
Fernwick: https://fernwick.com.au/ (like Our services section).
Industry/Entity Type
Mortgage, Property, Conveyancing, Property Investment
Coding
Coded - Design and coding required
Number of Pages Required
5+ page
Requirements
Must have
- Built for Wordpress and Elementor.
Nice to have
- See Project Description for links to ideas/elements that we have liked. However, open to ideas as long as the follow the navigation set out in the wire frame.

```html
<!DOCTYPE html>
<html lang="en">
<head>
<meta charset="utf-8">
<title>BlueCanopy Group – Finance, Property, Conveyancing</title>
<link href="https://fonts.googleapis.com/css2?family=Figtree:wght@400;500;600;700;800&family=Arimo:wght@400;700&display=swap" rel="stylesheet">
<style>
:root{
  --navy:#0b4a7e;
  --navy-deep:#0a3a63;
  --blue:#1170c4;
  --ink:#1b1b1b;
  --muted:#555;
  --paper:#fbfbf7;
  --white:#fff;
  --line:#d8d8d8;
  --star:#f5a623;
}
*{box-sizing:border-box;margin:0;padding:0}
html,body{width:1200px;height:3842px;overflow:hidden}
body{position:relative;background:var(--paper);font-family:"Arimo",Arial,sans-serif;color:var(--ink)}
.abs{position:absolute}
h1,h2,h3,.head{font-family:"Figtree",Arial,sans-serif}
.btn{position:absolute;display:flex;align-items:center;justify-content:center;background:var(--blue);color:var(--white);font-family:"Figtree",Arial,sans-serif;font-weight:700;font-size:13px}
.btn.ghost{background:var(--white);color:var(--blue);font-weight:500}
.ph{position:absolute}

/* header */
.site-header{top:0;left:0;width:1200px;height:103px;background:var(--paper)}
.brand{left:84px;top:30px;display:flex;align-items:center;gap:10px}
.brand-mark{width:36px;height:36px;background:var(--navy)}
.brand-name{font-family:"Figtree",Arial,sans-serif;font-weight:600;font-size:27px;color:var(--navy);line-height:1}
.nav{left:555px;top:43px;display:flex;gap:53px;font-size:13px;font-family:"Figtree",Arial,sans-serif}

/* hero */
.hero{top:103px;left:0;width:1200px;height:583px}
.hero-photo{left:0;top:0;width:1200px;height:583px;background:linear-gradient(160deg,#4d6a2f 0%,#6f8b45 35%,#3f5a25 70%,#27381a 100%)}
.hero-panel{left:607px;top:0;width:510px;height:583px;background:rgba(8,10,12,.88)}
.fullscreen{left:83px;top:38px;color:#eee;font-size:13px;display:flex;align-items:center;gap:14px}
.hero-title{left:70px;top:118px;font-family:"Figtree",Arial,sans-serif;font-weight:800;font-size:108px;line-height:108px;color:rgba(255,255,255,.72)}
.hero-sub{left:78px;top:380px;font-family:"Figtree",Arial,sans-serif;font-weight:300;font-size:70px;line-height:72px;color:rgba(255,255,255,.45);width:1000px}
.hero-rule{left:656px;top:195px;width:3px;height:126px;background:var(--blue)}
.hero-head{left:686px;top:195px;font-weight:700;font-size:40px;line-height:46px;color:var(--white)}
.hero-tag{left:686px;top:300px;font-size:16px;color:#e6e6e6;font-family:"Figtree",Arial,sans-serif}

/* services */
.services{top:686px;left:0;width:1200px;height:419px;background:var(--navy)}
.sec-title{position:absolute;width:100%;text-align:center;font-weight:700;font-size:31px}
.card{position:absolute;top:116px;width:290px;height:249px;background:var(--white);text-align:center}
.card svg{margin-top:30px}
.card h3{font-weight:500;font-size:21px;margin-top:12px}
.card p{font-size:15px;color:#333;margin-top:12px;line-height:18px;padding:0 40px}

/* why */
.why-photo1{left:83px;top:1188px;width:381px;height:443px;background:linear-gradient(180deg,#c5d6e6,#7f9db8)}
.why-photo2{left:217px;top:1464px;width:247px;height:167px;background:linear-gradient(135deg,#4a6f97,#c9a15a);border-left:7px solid var(--paper);border-top:7px solid var(--paper)}
.why-title{left:519px;top:1222px;font-weight:700;font-size:31px}
.why-item{left:519px;width:600px}
.why-item h4{color:var(--blue);font-family:"Figtree",Arial,sans-serif;font-weight:600;font-size:16px}
.why-item p{font-size:12px;line-height:14px;margin-top:8px;color:#333}

/* subscribe */
.subscribe{top:1715px;left:0;width:1200px;height:211px;background:linear-gradient(90deg,#0d2f4f,#2b5d86 60%,#5d7e97)}
.subscribe h2{position:absolute;left:83px;top:52px;color:var(--white);font-weight:600;font-size:29px}
.field{position:absolute;top:116px;height:40px;background:var(--white);font-size:12px;color:#999;padding:13px 14px}

/* team */
.team{top:1926px;left:0;width:1200px;height:513px;background:var(--navy)}
.team h2{position:absolute;left:83px;top:165px;color:var(--white);font-weight:700;font-size:31px}
.team .lead{position:absolute;left:83px;top:225px;color:var(--white);font-size:20px;line-height:24px;width:410px;font-family:"Figtree",Arial,sans-serif}
.member{position:absolute;top:84px;width:191px;text-align:center;color:var(--white)}
.member .photo{height:249px;background:linear-gradient(180deg,#eef0f2,#cfd4d9);border-radius:0 0 60px 60px}
.member b{display:block;margin-top:16px;font-size:13px;font-family:"Figtree",Arial,sans-serif}
.member span{display:block;margin-top:8px;font-size:11px;color:#cfdbe8}
.dots{position:absolute;left:784px;top:423px;display:flex;gap:14px}
.dots i{width:6px;height:6px;border-radius:50%;background:#9bb4cc}
.dots i:first-child{background:var(--white)}

/* articles */
.articles-title{top:2517px}
.article{position:absolute;top:2584px;width:328px;height:341px;background:var(--white);box-shadow:0 2px 6px rgba(0,0,0,.15)}
.article h3{position:absolute;left:20px;top:26px;right:20px;font-weight:500;font-size:16px;line-height:20px}
.article a{position:absolute;left:20px;top:76px;font-size:12px;color:var(--blue)}
.article .thumb{position:absolute;left:0;top:107px;width:328px;height:234px}

/* reviews */
.rule{left:0;width:1200px;height:2px;background:var(--line)}
.reviews-title{left:83px;top:3110px;font-weight:700;font-size:30px}
.badge{position:absolute;width:60px;height:60px;border-radius:50%}
.rating{position:absolute;font-size:13px;line-height:19px;text-align:center}
.rating .score{font-size:19px;display:flex;align-items:center;gap:6px}

/* family band */
.family{left:0;top:3253px;width:1200px;height:250px;background:linear-gradient(180deg,#8fc3e0,#5c9ec7 45%,#e2c7a8 75%,#c99a78)}

/* footer */
.footer{top:3503px;left:0;width:1200px;height:339px;background:var(--navy);color:var(--white);font-family:"Figtree",Arial,sans-serif}
.fcol{position:absolute;top:100px}
.fcol h4{font-size:16px;font-weight:600;text-decoration:underline;margin-bottom:22px}
.fcol li{list-style:none;font-size:16px;line-height:26px}
.frow{display:flex;gap:8px;align-items:flex-start;font-size:16px;line-height:19px}
.small{font-size:12px;padding-left:26px;line-height:18px;margin-bottom:10px}
.social{width:22px;height:22px;border-radius:50%;background:var(--white)}
</style>
</head>
<body>

<header class="abs site-header">
  <div class="abs brand"><span class="brand-mark"></span><span class="brand-name">BlueCanopy</span></div>
  <nav class="abs nav"><span>Finance</span><span>Property</span><span>Commercials</span><span>About</span></nav>
  <div class="btn" style="left:993px;top:31px;width:124px;height:41px">Contact Us</div>
</header>

<section class="abs hero">
  <div class="ph hero-photo" role="img" aria-label="Background video still of tall green grass"></div>
  <div class="abs hero-panel"></div>
  <div class="abs fullscreen">Fullscreen
    <svg width="24" height="24" viewBox="0 0 24 24" fill="none" stroke="#fff" stroke-width="2.4"><path d="M2 8V2h6M16 2h6v6M22 16v6h-6M8 22H2v-6"/></svg>
  </div>
  <h1 class="abs hero-title">BlueCanopy<br>Group</h1>
  <p class="abs hero-sub">A trusted team for your<br>property &amp; home loan journey</p>
  <div class="abs hero-rule"></div>
  <h2 class="abs hero-head">Finance, Property,<br>Conveyancing –</h2>
  <p class="abs hero-tag">Unlocking Opportunities and solving problems.</p>
  <div class="btn" style="left:687px;top:347px;width:123px;height:41px">Contact Us</div>
  <div class="btn ghost" style="left:825px;top:347px;width:131px;height:41px">Our Services</div>
</section>

<section class="abs services">
  <h2 class="sec-title" style="top:54px;color:var(--white)">– Our Services –</h2>
  <div class="card" style="left:150px">
    <svg width="40" height="42" viewBox="0 0 40 42" fill="none" stroke="#1170c4" stroke-width="2.2"><path d="M14 4h12l-4 8h-4z"/><ellipse cx="20" cy="27" rx="16" ry="13"/><text x="20" y="33" font-size="16" text-anchor="middle" fill="#1170c4" stroke="none" font-family="Arial">$</text></svg>
    <h3>Finance</h3><p>for your home, car, investments, and assets</p>
    <div class="btn" style="left:26px;top:180px;width:238px;height:42px">Learn More</div>
  </div>
  <div class="card" style="left:455px">
    <svg width="44" height="42" viewBox="0 0 44 42" fill="none" stroke="#1170c4" stroke-width="2.4"><path d="M4 38L16 24l8 6L38 8M30 8h8v8M8 38V28M16 38V30M24 38V32"/></svg>
    <h3>Property</h3><p>sales, purchases, and rentals</p>
    <div class="btn" style="left:26px;top:180px;width:238px;height:42px">Learn More</div>
  </div>
  <div class="card" style="left:760px">
    <svg width="44" height="42" viewBox="0 0 44 42" fill="none" stroke="#1170c4" stroke-width="2.2"><rect x="2" y="10" width="40" height="28"/><path d="M14 10V3h16v7M14 10v28M30 10v28"/></svg>
    <h3>Conveyancing</h3><p>for seamless property transactions</p>
    <div class="btn" style="left:26px;top:180px;width:238px;height:42px">Learn More</div>
  </div>
</section>

<div class="ph why-photo1" role="img" aria-label="Family photo of parents and children forming a roof shape"></div>
<div class="ph why-photo2" role="img" aria-label="Photo of a couple holding new house keys"></div>
<h2 class="abs why-title">– Why Choose Us –</h2>
<div class="abs why-item" style="top:1288px"><h4>20 years experience</h4><p>We have grown and changed with the industry, and we're dedicated to continually improve our service and products so you get the best solutions possible.</p></div>
<div class="abs why-item" style="top:1372px"><h4>We give you choice</h4><p>Working with over 20 large and small lenders, property developers and switched on accountants, we have the scope to give you good choices for the future.</p></div>
<div class="abs why-item" style="top:1456px"><h4>It is about the outcome</h4><p>We have grown and changed with the industry, and we're dedicated to continually improve our service and products so you get the best solutions possible.</p></div>
<div class="abs why-item" style="top:1540px"><h4>We give you options that makes sense</h4><p>Working with over 20 large and small lenders, property developers and switched on accountants, we have the scope to give you good choices for the future.</p></div>

<section class="abs subscribe">
  <h2>Subscribe to Keep Up to Date on Market News</h2>
  <div class="field" style="left:83px;width:336px">Your name*</div>
  <div class="field" style="left:432px;width:336px">Your email*</div>
  <div class="btn" style="left:781px;top:116px;width:336px;height:40px">Subscribe Now</div>
</section>

<section class="abs team">
  <h2>– Your Dream, Our Team! –</h2>
  <p class="lead">A trusted team for your property and home loan journey.</p>
  <div class="btn" style="left:83px;top:303px;width:150px;height:41px">Meet Our Team</div>
  <div class="member" style="left:519px"><div class="photo" role="img" aria-label="Portrait of the general manager"></div><b>Owen Kessler</b><span>General manager</span></div>
  <div class="member" style="left:723px"><div class="photo" role="img" aria-label="Portrait of the group manager"></div><b>Clara Wendell</b><span>Group manager</span></div>
  <div class="member" style="left:926px"><div class="photo" role="img" aria-label="Portrait of the licensed conveyancer"></div><b>Nadia Fairbrook</b><span>Licensed conveyancer</span></div>
  <div class="dots"><i></i><i></i><i></i><i></i></div>
</section>

<h2 class="sec-title articles-title">– Newest Articles –</h2>
<article class="article" style="left:86px"><h3>Credit Scores - What Are They and How Do They Affect You</h3><a>Read more</a><div class="thumb" role="img" aria-label="Article image of a woman shrugging on a yellow background" style="background:linear-gradient(135deg,#f2c335,#d99a25)"></div></article>
<article class="article" style="left:435px"><h3>Poor Credit Home Loan Refinance</h3><a>Read more</a><div class="thumb" role="img" aria-label="Article image of a credit rating form with glasses and calculator" style="background:linear-gradient(135deg,#c9343a,#e9e4dc 55%,#3ab77a)"></div></article>
<article class="article" style="left:786px"><h3>Understanding Appraisals</h3><a>Read more</a><div class="thumb" role="img" aria-label="Article image of a woman using a tablet to appraise a house" style="background:linear-gradient(135deg,#cfd7de,#6e8aa6)"></div></article>

<div class="abs rule" style="top:3008px"></div>
<h2 class="abs reviews-title">– What Our Clients Say About Us –</h2>
<div class="badge" style="left:618px;top:3078px;background:#7dbb3c"></div>
<div class="rating" style="left:680px;top:3078px;width:180px">
  <div class="score">5.0 <svg width="106" height="18" viewBox="0 0 106 18"><g fill="#f5a623"><path id="st" d="M9 1l2.4 5.2 5.6.6-4.2 3.8 1.2 5.6L9 13.4 4 16.2l1.2-5.6L1 6.8l5.6-.6z"/><use href="#st" x="21"/><use href="#st" x="42"/><use href="#st" x="63"/><use href="#st" x="84"/></g></svg></div>
  Rated 5.0 out of 5 on<br>ratingsdesk.com.au
</div>
<div class="btn" style="left:670px;top:3167px;width:121px;height:27px">Read Review</div>
<div class="badge" style="left:880px;top:3078px;background:var(--navy)"></div>
<div class="rating" style="left:950px;top:3078px;width:160px">
  <div class="score">4.9 <svg width="106" height="18" viewBox="0 0 106 18"><g fill="#f5a623"><use href="#st"/><use href="#st" x="21"/><use href="#st" x="42"/><use href="#st" x="63"/><use href="#st" x="84"/></g></svg></div>
  Rated 4.9 out of 5 on<br>Lookup Reviews
</div>
<div class="btn" style="left:931px;top:3167px;width:122px;height:27px">Read Review</div>
<div class="abs rule" style="top:3246px"></div>

<div class="ph family" role="img" aria-label="Smiling family of four at the beach"></div>

<footer class="abs footer">
  <div class="fcol" style="left:83px"><h4>Quick Links</h4><ul><li>Finance</li><li>Property</li><li>Commercials</li><li>About</li><li>Contact Us</li></ul></div>
  <div class="fcol" style="left:306px"><h4>Opening Times</h4>
    <div class="frow"><svg width="18" height="18" viewBox="0 0 18 18" fill="none" stroke="#fff" stroke-width="1.6"><circle cx="9" cy="9" r="7.5"/><path d="M9 4.5V9l3 2"/></svg>Monday - Friday</div>
    <div class="small">9a.m-5p.m</div>
    <div class="frow"><svg width="18" height="18" viewBox="0 0 18 18"><circle cx="9" cy="9" r="8.5" fill="#fff"/><rect x="4" y="8" width="10" height="2.2" fill="#0b4a7e"/></svg>Saturday - Sunday</div>
    <div class="small">Closed</div>
  </div>
  <div class="fcol" style="left:595px"><h4>Contact Us</h4>
    <div class="frow" style="margin-bottom:8px"><svg width="18" height="18" viewBox="0 0 18 18"><rect x="1" y="3" width="16" height="12" fill="#fff"/><path d="M1 4l8 6 8-6" fill="none" stroke="#0b4a7e" stroke-width="1.4"/></svg>info@bluecanopy.com.au</div>
    <div class="frow"><svg width="18" height="18" viewBox="0 0 18 18" fill="#fff"><path d="M4 1.5l3 3-2 2.2c1 2.3 2.8 4.1 5.2 5.2l2.2-2 3 3-2.2 2.6C7.5 15.2 2.8 10.5 1.5 3.7z"/></svg>1300 418 207</div>
  </div>
  <div class="fcol" style="left:913px"><h4>Reach Us</h4>
    <div class="frow"><svg width="18" height="20" viewBox="0 0 18 20" fill="#fff"><path d="M9 1a6 6 0 0 0-6 6c0 4.5 6 12 6 12s6-7.5 6-12a6 6 0 0 0-6-6zm0 8.2a2.2 2.2 0 1 1 0-4.4 2.2 2.2 0 0 1 0 4.4z"/></svg>4C Larchmont Lane,<br>Ashgrove Park, VIC 3170</div>
    <div style="display:flex;gap:18px;margin-top:14px"><span class="social"></span><span class="social"></span></div>
  </div>
</footer>

</body>
</html>
```